Harbor Ridge Seed Collective business cards

Create a single-sided business card for the Harbor Ridge Seed Collective based on the attached logo.
The additional data fields include Name, Title, Email, Phone, and website.
Please use the following as sample data:
Name: Dana Vellor
Title: Co-Founder / Investor
Email: danavellor@mailbrook.example
Phone: 805-555-0147
Website: www.hrseedcollective.example

Target Market(s)

Start ups, entrepreneurs, venture capitalists

Industry/Entity Type

Investment

Contact Information for Business Card

Professional business card. Technology company.

Font styles to use
Serif
Sans Serif

Requirements
Must have
• Include the HRSC logo (attached)
• Name
• Title
• Email
• Phone
• Website
Should not have
• Cute, cartoony

```html
<!DOCTYPE html>
<html lang="en">
<head>
<meta charset="utf-8">
<title>Harbor Ridge Seed Collective — Business Card</title>
<link rel="stylesheet" href="https://fonts.googleapis.com/css2?family=Source+Sans+3:wght@400;600;700&display=swap">
<style>
  :root {
    --brand-green: #1b873b;
    --ink-dark: #414042;
    --text-body: #3a3a3c;
    --card-white: #ffffff;
    --backdrop: #e9eaec;
  }
  * { box-sizing: border-box; margin: 0; padding: 0; }
  html, body {
    width: 1025px;
    height: 1200px;
    overflow: hidden;
    background: var(--backdrop);
    font-family: "Source Sans 3", sans-serif;
  }
  .canvas { position: relative; width: 1025px; height: 1200px; }

  .card {
    position: absolute;
    left: 118px;
    width: 782px;
    height: 446px;
    background: var(--card-white);
    border-radius: 24px;
    overflow: hidden;
    box-shadow: 0 4px 14px rgba(0,0,0,0.12);
  }
  .card--front { top: 114px; }
  .card--back  { top: 630px; }

  .card__waves { position: absolute; inset: 0; width: 100%; height: 100%; }

  .brand {
    position: absolute;
    display: flex;
    align-items: center;
    gap: 20px;
  }
  .brand__dot {
    width: 58px;
    height: 58px;
    border-radius: 50%;
    background: var(--brand-green);
    flex: none;
  }
  .brand__name {
    color: var(--brand-green);
    font-weight: 600;
    font-size: 31px;
    line-height: 1.12;
    letter-spacing: 0.5px;
  }
  .card--front .brand { left: 34px; top: 42px; }
  .card--back .brand { left: 50%; top: 50%; transform: translate(-50%, -50%); }
  .card--back .brand__dot { width: 72px; height: 72px; }
  .card--back .brand__name { font-size: 36px; }

  .holder { position: absolute; left: 32px; top: 264px; }
  .holder__name {
    color: var(--brand-green);
    font-weight: 700;
    font-size: 23px;
    letter-spacing: 0.3px;
  }
  .holder__title {
    color: var(--text-body);
    font-size: 22px;
    margin-top: 2px;
  }

  .contact {
    position: absolute;
    right: 24px;
    top: 324px;
    list-style: none;
    color: #fff;
    font-size: 19.5px;
    text-align: right;
  }
  .contact__item {
    display: flex;
    align-items: center;
    justify-content: flex-end;
    gap: 12px;
    height: 29px;
  }
  .contact__icon { width: 18px; height: 18px; flex: none; }
</style>
</head>
<body>
<main class="canvas">

  <section class="card card--front" aria-label="Business card front">
    <svg class="card__waves" viewBox="0 0 782 446" preserveAspectRatio="none" aria-hidden="true">
      <path d="M0,382 C260,420 500,372 782,22 L782,446 L0,446 Z" fill="var(--brand-green)"/>
      <path d="M0,334 C110,382 330,382 548,250 C360,364 160,400 0,370 Z" fill="var(--ink-dark)"/>
    </svg>

    <div class="brand">
      <span class="brand__dot"></span>
      <div class="brand__name">Harbor Ridge<br>Seed Collective</div>
    </div>

    <div class="holder">
      <p class="holder__name">DANA VELLOR</p>
      <p class="holder__title">Co-Founder / Investor</p>
    </div>

    <ul class="contact">
      <li class="contact__item">
        <span>805-555-0147</span>
        <svg class="contact__icon" viewBox="0 0 20 20" aria-hidden="true">
          <path d="M2,7 C2,3 18,3 18,7 L15,8 L14,6 L6,6 L5,8 Z" fill="#fff"/>
          <path d="M5,10 L7,7.5 L13,7.5 L15,10 L16,16 L4,16 Z" fill="#fff"/>
          <circle cx="10" cy="11.5" r="1.8" fill="var(--brand-green)"/>
        </svg>
      </li>
      <li class="contact__item">
        <span>danavellor@mailbrook.example</span>
        <svg class="contact__icon" viewBox="0 0 20 20" aria-hidden="true">
          <rect x="1.5" y="5" width="17" height="11" rx="1" fill="#fff"/>
          <path d="M2,6 L10,11.5 L18,6" fill="none" stroke="var(--brand-green)" stroke-width="1.6"/>
        </svg>
      </li>
      <li class="contact__item">
        <span>www.hrseedcollective.example</span>
        <svg class="contact__icon" viewBox="0 0 20 20" aria-hidden="true">
          <g fill="none" stroke="#fff" stroke-width="1.5">
            <circle cx="10" cy="10" r="8"/>
            <ellipse cx="10" cy="10" rx="3.6" ry="8"/>
            <line x1="2" y1="10" x2="18" y2="10"/>
            <path d="M3.5,6 H16.5 M3.5,14 H16.5"/>
          </g>
        </svg>
      </li>
    </ul>
  </section>

  <section class="card card--back" aria-label="Business card back">
    <div class="brand">
      <span class="brand__dot"></span>
      <div class="brand__name">Harbor Ridge<br>Seed Collective</div>
    </div>
  </section>

</main>
</body>
</html>
```